Bramblewood Coatings of Central Florida, LLC. Start-up painting business needs a professional web desig

We have a start up painting business that would like to reach/focus on commercial clients like building contractors, HOA's, apartment complexes, etc.. We would like a residential aspect to the web design as well. We have an existing website at "trybramblewoodcoats.com" with usable content. Have logo and color scheme attached. Use provided website ONLY as template. Add commercial services page. Can type own content when needed.

Industry/Entity Type

Apartment

Number of Pages Required

5+ page

Font styles to use
Serif
Sans Serif
Decorative
Script

Requirements
Must have
• Commercial services

```html
<!DOCTYPE html>
<html lang="en">
<head>
<meta charset="utf-8">
<title>Bramblewood Coatings of Central Florida, LLC</title>
<link href="https://fonts.googleapis.com/css2?family=Pathway+Gothic+One&family=Rokkitt:wght@400&family=Roboto:wght@400&display=swap" rel="stylesheet">
<style>
:root{
  --olive:#6b6a3e;
  --olive-dark:#5d5c35;
  --rose:#d99a88;
  --blush:#f2ddd7;
  --ink:#2e2a26;
  --brown:#3b2a22;
  --text:#333;
  --white:#fff;
  --footer:#111;
  --panel:#f1f1f1;
}
*{margin:0;padding:0;box-sizing:border-box}
html,body{width:1200px;height:989px;overflow:hidden;background:var(--white)}
body{position:relative;font-family:"Roboto",Arial,sans-serif;color:var(--text)}
.abs{position:absolute}

.topbar{left:0;top:0;width:1200px;height:41px;background:var(--olive)}
.topbar-rule{left:0;top:42px;width:1200px;height:3px;border-top:1px solid var(--rose);border-bottom:1px solid var(--rose)}
.tagline{left:291px;top:13px;font-family:"Rokkitt",Georgia,serif;font-size:15px;color:var(--white);letter-spacing:.3px;white-space:nowrap}
.phone{left:855px;top:8px;display:flex;align-items:center;gap:8px;color:var(--white);font-size:21px;white-space:nowrap}

.brand-mark{left:160px;top:10px;width:126px;height:115px;border-radius:50%;background:var(--white)}
.brand-name{left:291px;top:55px;font-family:"Pathway Gothic One",sans-serif;font-size:29px;line-height:31px;color:var(--olive);letter-spacing:.5px;text-transform:uppercase;white-space:nowrap}

.nav{left:610px;top:85px;display:flex;align-items:center;font-size:13px;color:var(--ink);white-space:nowrap}
.nav a{color:inherit;text-decoration:none;margin-right:26px}
.nav a.active{background:var(--olive);color:var(--white);padding:5px 15px;border-radius:2px;margin-right:30px}

.hero{left:0;top:130px;width:1200px;height:397px;background:linear-gradient(90deg,#8a6a48 0%,#c9ab86 30%,#e6dccf 50%,#d9b98e 70%,#b58b5a 100%)}
.hero-title{left:300px;top:246px;width:512px;text-align:center;font-size:27px;line-height:32px;color:var(--ink);text-transform:uppercase}
.arrow{top:308px;width:42px;height:34px;background:rgba(255,255,255,.35);display:flex;align-items:center;justify-content:center}
.arrow span{width:32px;height:28px;background:#333;display:flex;align-items:center;justify-content:center;border-radius:2px}
.arrow-left{left:0}.arrow-right{left:1156px}

.tab{top:481px;width:246px;height:46px;font-family:"Rokkitt",Georgia,serif;font-size:19px;line-height:24px;padding:14px 12px 0;color:var(--ink);background:rgba(225,220,215,.85);text-transform:uppercase;white-space:nowrap;overflow:hidden}
.tab.current{background:rgba(107,106,62,.85);color:var(--white)}

.gallery-strip{left:159px;top:527px;width:882px;height:177px;background:linear-gradient(180deg,#f7f7f7,#ececec)}
.thumb{top:562px;width:154px;height:123px;border:1px solid #444;background:var(--white);padding:4px}
.thumb div{width:100%;height:100%}

.welcome{left:0;top:704px;width:1200px;height:215px;background:var(--blush)}
.welcome h1{position:absolute;left:0;top:20px;width:1200px;text-align:center;font-family:"Pathway Gothic One",sans-serif;font-weight:400;font-size:29px;color:var(--brown);text-transform:uppercase;white-space:nowrap}
.welcome p{position:absolute;left:185px;top:88px;width:830px;text-align:center;font-size:12.5px;line-height:22px;color:var(--text)}
.read-more{left:561px;top:870px;width:78px;height:25px;background:var(--olive);color:var(--white);font-size:13px;text-align:center;line-height:25px;border-radius:2px;white-space:nowrap}

.footer{left:0;top:919px;width:1200px;height:66px;background:var(--footer);color:var(--white)}
.footer-rule{left:0;top:985px;width:1200px;height:4px;background:var(--rose)}
.footer-links{left:166px;top:932px;font-size:13px;color:var(--white);display:flex;gap:18px;white-space:nowrap}
.copyright{left:166px;top:957px;font-size:12px;color:var(--white);white-space:nowrap}
.follow{left:666px;top:946px;font-size:12px;color:var(--white);white-space:nowrap}
.social{top:938px;width:28px;height:28px;border-radius:3px}
.footer-mark{left:975px;top:928px;width:48px;height:48px;border-radius:50%;background:#3a3a3a}
</style>
</head>
<body>
<div class="abs topbar"></div>
<div class="abs topbar-rule"></div>
<div class="abs tagline">WHERE DREAMS MEET REALITY</div>
<div class="abs phone">
  <svg width="24" height="24" viewBox="0 0 24 24" aria-hidden="true"><circle cx="12" cy="12" r="11" fill="none" stroke="#fff" stroke-width="1.3"/><path d="M9 6c-1 1-2 2 0 6s5 6 6 6l2-2-2-2-2 1c-1-1-3-3-3-4l1-2z" fill="#fff"/></svg>
  <span>+1.555-014-2876</span>
</div>

<div class="abs brand-mark"></div>
<div class="abs brand-name">Bramblewood Coatings of<br>Central Florida, LLC.</div>

<nav class="abs nav">
  <a class="active" href="#">HOME</a>
  <a href="#">ABOUT US</a>
  <a href="#">SERVICES</a>
  <a href="#">GALLERY</a>
  <a href="#">CONTACT US</a>
</nav>

<div class="abs hero" role="img" aria-label="Bright painted living room with sofa, cabinet and ocean-view windows"></div>
<div class="abs hero-title">Providing quality work at affordable prices</div>
<div class="abs arrow arrow-left"><span><svg width="10" height="14" viewBox="0 0 10 14"><path d="M8 1L2 7l6 6" fill="none" stroke="#fff" stroke-width="2.5"/></svg></span></div>
<div class="abs arrow arrow-right"><span><svg width="10" height="14" viewBox="0 0 10 14"><path d="M2 1l6 6-6 6" fill="none" stroke="#fff" stroke-width="2.5"/></svg></span></div>

<div class="abs tab current" style="left:160px">Residential Painting</div>
<div class="abs tab" style="left:432px">Commercial Painting</div>
<div class="abs tab" style="left:706px;padding-left:22px">Heritage Painting</div>

<div class="abs gallery-strip"></div>
<div class="abs thumb" style="left:175px"><div role="img" aria-label="Foyer with staircase and wood floor" style="background:linear-gradient(135deg,#e9d3a6,#9a6a3a)"></div></div>
<div class="abs thumb" style="left:348px"><div role="img" aria-label="Painter working on a house gable" style="background:linear-gradient(180deg,#3d6fb5,#c7cdd6)"></div></div>
<div class="abs thumb" style="left:521px"><div role="img" aria-label="Yellow hallway with built-in shelves" style="background:linear-gradient(135deg,#e8c55a,#b6772f)"></div></div>
<div class="abs thumb" style="left:694px"><div role="img" aria-label="Freshly painted house with front lawn" style="background:linear-gradient(180deg,#c5d3e4,#b9a68a 55%,#4f8a34)"></div></div>
<div class="abs thumb" style="left:866px"><div role="img" aria-label="White staircase with potted plant" style="background:linear-gradient(135deg,#f1ecdc,#b8a27a)"></div></div>

<section class="abs welcome">
  <h1>Welcome to Bramblewood Coatings of Central Florida, LLC</h1>
  <svg class="abs" style="left:437px;top:60px" width="346" height="18" viewBox="0 0 346 18" aria-hidden="true"><line x1="0" y1="4" x2="346" y2="4" stroke="#d99a88"/><line x1="0" y1="8" x2="346" y2="8" stroke="#d99a88"/><path d="M167 6l6 9 6-9" fill="none" stroke="#d99a88"/></svg>
  <p>Bramblewood Coatings of Central Florida, LLC. has painted thousands of homes in its day, but the one we’re most excited about painting is the one we’re painting today. Your home could be that home.At Bramblewood Coatings of Central Florida, we strive to exceed the expectations of each and every customer. We do that by using the highest quality products and through out attention to detail.</p>
  <svg class="abs" style="left:476px;top:175px" width="248" height="6" viewBox="0 0 248 6" aria-hidden="true"><line x1="0" y1="1" x2="248" y2="1" stroke="#c9bcb8"/><line x1="0" y1="4" x2="248" y2="4" stroke="#c9bcb8"/></svg>
</section>
<div class="abs read-more">Read More</div>

<footer class="abs footer"></footer>
<div class="abs footer-links"><span>• Home</span><span>• About Us</span><span>• Services</span><span>• Gallery</span><span>• Contact Us</span></div>
<div class="abs copyright">Copyright ©2015, BramblewoodCoatingsofCentralFlorida.&nbsp; All Rights Reserved</div>
<div class="abs follow">Follow Us On</div>
<div class="abs social" style="left:749px;background:#3b5a9a" aria-label="Social profile"></div>
<div class="abs social" style="left:783px;background:#4aa3d8" aria-label="Social profile"></div>
<div class="abs social" style="left:817px;background:#c8402e" aria-label="Social profile"></div>
<div class="abs footer-mark"></div>
<div class="abs footer-rule"></div>
</body>
</html>
```